Neue Visitenkarten für internationales Beratungsunternehmen
Zielgruppe
Management Consulting, Management Beratung. Insgesamt beinhaltet das Portfolio wirklich Unternehmensberatung von der Vision zu Strategie, von der Strategie zu Businesss Architektur und Unternehmenszielen über Prozesse zu Prozessziele, Unternehmens(re)organisation bis hin zu IT Architektur und IT Beratung.
Prozessanalyse und Business Analyse sind wichtige Teile. IT Architektur beinhaltet all diese Aufgaben in der Software Beratung von der fachlichen Konzeption bis zur Implementierung bzw. Software Solution Design, Implementierung und Wartung, also das gesamte Software Life Cycle. Es handelt sich also um den Weg, wie man aus einer Vision ein IT-enabled Unternehmen aufzieht und zum Laufen bringt. Wir möchten Richtungsweisend sein in der Ausrichtung der Business Architektur, der Organisation, der Dienstleistungserbringung und der IT. Prozess-Überwachung (Reporting) und Prozess-Zertifizierung ist ein weitere Pfeiler. Wir bleiben immer am Puls des Unternehmens und am Puls seiner Prozesse. Das Ergebnis unserer Dienstleistung ist eine Lean IT enabled Solution und auch eine Lean Company. Da wir vieles anders machen ist unser Slogan 'We leave own tracks behind as we break new ground'. Es kann aber bald ein anderes folgen, wie 'Ihr Erfolg ist unser Ziel'.
Zur Zielgruppe gehören alle Mittelstands- und Großunternehmen, die ihr Business neu organisieren wollen, wie auch neu gegründete Unternehmen, die vom Anfang an ein Prozessorientiertes Vorgehen für Ihr Business anstreben. Diese Unternehmen können sowohl Dienstleistungen anbieten als auch aus dem produzierenden Gewerbe sein. Beispielhaft: aus After Sales oder sonstigen Services, Automotive, Versicherungen, Banken, Luftfahrt, Universitäten, Bildung, Chemie, Forschung, Medizin und Pharma und vieles mehr. Eine Einschränkung zur Zeit nicht angedacht. Neugründungen sind auf jeden Fall interessant. Es geht hauptsächlich um die Management Beratung und die Produktiv-Setzung solcher Firmen.
Aufgabenstellung
Das Projekt soll
1. ein Visitenkarte (fertig verwendbares und änderbares Template) und
2. ein entsprechend ansprechendes Briefpapier zum vordrucken für eine visionäre Firma finden und
3. soll das bisherige Logo und CI Farben einbinden und
4. nach Bedarf weitere passende Farben dazu finden.
Das Logo erhalten Sie hier von mir als RGB und CMYK *.pdf, und als *.psd, *.eps, *.ai auf Anforderung nachträglich zugesendet.
5. Das bevorzugte Logo ist das 2. oder 1. in der linken Spalte.
6. Die Unternehmensdaten für das Briefpapier finden Sie im angehängten Word-Dokument.
USt-Id und St-Nr werde noch vom FA vergeben. Diese zwei Werte sollten im Nachhinein noch anpassbar sein. Das wäre praktisch auch für alle anderen Texte (z.B. bei einem Firmenumzug).
7. Die Visitenkarte sollte folgende Angaben berücksichtigen:
Veltrano GmbH
www.veltrano-example.com
8. Ggf. Slogans wie die folgenden könnten verwendet werden:
The Harbor Weavers (ist bereits im Logo)
Lassen Sie Ihre Vision wahr werden
Veltrano® - Der Weg zum Erfolg
Business Process Solutions
9. Sollten Sie noch ein QR Code für gut finden oder eine sonstige Besonderheit, wie Klappkarten, so können wir das im Zuge des Projektes klären.
10. Hier kommen die CI Farben und Font Angaben: styleguide
Farben
* BLAUn (Azul)
CMYK - 76 - 19 0 86 in %
RGB - 14 - 42 - 65
RAL (Näherungswert) - Stahlblau 5011 ( Saphirblau 5003 , Schwarzblau 5004)
* Graun (Gris)
CMYK - 0 - 0 - 0 - 60 in %
RGB - 143 - 144 - 143
RAL (Näherungswert) - Verkehrsgrau 7042
Schriften (Fonts)
* Wortmarke (Logo) - Century Gothic Regular (Ableitung)
Diese Schrift sollte auch beim Firmennahmen bei der Adresse verwendet werden.
* Slogan - Open sans (google font)

```html
<!DOCTYPE html>
<html lang="de">
<head>
<meta charset="utf-8">
<title>Veltrano Briefpapier und Kuvert</title>
<link href="https://fonts.googleapis.com/css2?family=Questrial&family=Open+Sans:wght@400;600;700&display=swap" rel="stylesheet">
<style>
:root{
  --ci-blue:#0e2a41;
  --ci-grey:#8f908f;
  --accent-blue:#3b8fc6;
  --band-grey:#4a4d51;
  --ink:#2b2b2b;
  --paper:#ffffff;
  --stage:#ecebe8;
}
*{margin:0;padding:0;box-sizing:border-box}
html,body{width:1200px;height:800px;overflow:hidden;background:var(--stage);font-family:"Open Sans",sans-serif;color:var(--ink)}
.canvas{position:relative;width:1200px;height:800px}

/* letterhead */
.letterhead{position:absolute;left:45px;top:24px;width:526px;height:743px;background:var(--paper);box-shadow:0 2px 8px rgba(0,0,0,.18)}
.letterhead .top-band{position:absolute;left:0;top:0;width:100%;height:8px;background:#a7a8a9}
.brand{position:absolute;font-family:"Questrial",sans-serif}
.brand .wordmark{display:flex;align-items:center;gap:8px;color:var(--ci-blue);letter-spacing:3px;line-height:1}
.brand .wordmark .dot{border-radius:50%;background:var(--ci-grey);flex:none}
.brand .tagline{color:var(--ci-grey);letter-spacing:2.2px;text-transform:uppercase;border-top:1px solid var(--ci-grey);margin-top:4px;padding-top:2px}
.letterhead .brand{left:43px;top:26px}
.letterhead .brand .wordmark{font-size:31px}
.letterhead .brand .dot{width:30px;height:30px}
.letterhead .brand .tagline{font-size:9.5px;margin-left:38px}
.sender{position:absolute;right:44px;top:40px;text-align:right;font-size:8.5px;line-height:9.5px;color:#555}
.sender .company{font-family:"Questrial",sans-serif;font-weight:700;color:var(--ci-blue)}
.contact-list{position:absolute;right:28px;top:72px;list-style:none;font-size:6px;color:#777}
.contact-list li{display:flex;justify-content:flex-end;align-items:center;gap:6px;height:17px}
.contact-list svg{width:10px;height:10px;fill:var(--ci-blue)}
.window-marks{position:absolute;left:42px;top:112px;width:226px;height:87px}
.window-marks span{position:absolute;width:12px;height:10px;border-color:#888;border-style:solid;border-width:0}
.window-marks .tl{left:0;top:0;border-left-width:1px;border-top-width:1px}
.window-marks .tr{right:0;top:0;border-right-width:1px;border-top-width:1px}
.window-marks .bl{left:0;bottom:0;border-left-width:1px;border-bottom-width:1px}
.window-marks .br{right:0;bottom:0;border-right-width:1px;border-bottom-width:1px}
.window-address{position:absolute;left:83px;top:127px;font-size:10px;line-height:15px;color:#555}
.return-line{position:absolute;left:43px;top:220px;width:246px;font-size:4.6px;color:#444;border-bottom:1px solid #333;padding-bottom:1px}
.recipient{position:absolute;left:43px;top:238px;font-size:9.5px;line-height:11.5px;color:#222}
.subject{position:absolute;left:44px;top:295px;font-size:8px;font-weight:700;color:#111}
.body-text{position:absolute;left:44px;font-size:7.5px;color:#333}
.fold-mark{position:absolute;left:0;width:18px;height:1px;background:#999}
.footer-brand{position:absolute;left:72px;top:680px;text-align:center;font-family:"Questrial",sans-serif;color:var(--ci-blue);font-size:8px;font-weight:700}
.footer-brand .dot{display:block;margin:0 auto 4px;width:16px;height:16px;border-radius:50%;background:var(--ci-grey)}
.footer-col{position:absolute;top:681px;font-size:6px;line-height:8px;color:var(--ci-blue)}
.footer-col.bank{left:180px}
.footer-col.tax{left:327px;top:684px}
.footer-col.branch{left:441px;top:684px;font-size:6.8px;line-height:8px}
.footer-divider{position:absolute;top:682px;width:1px;height:30px;background:#bbb}
.bands{position:absolute;display:flex;align-items:center}
.bands .rule{flex:1;position:relative;height:12px}
.bands .rule::before{content:"";position:absolute;left:0;right:0;top:0;height:2px;background:var(--accent-blue)}
.bands .rule::after{content:"";position:absolute;left:0;right:0;top:5px;height:7px;background:var(--band-grey)}
.bands .url{display:flex;align-items:center;gap:4px;padding:0 5px;font-family:"Open Sans",sans-serif;color:var(--ci-blue);white-space:nowrap}
.bands .url svg{fill:none;stroke:var(--ci-blue);stroke-width:1.3}
.letterhead .bands{left:0;right:0;top:718px}
.letterhead .bands .rule.short{flex:0 0 40px}
.letterhead .bands .url{font-size:11.5px}
.letterhead .bands .url svg{width:11px;height:11px}

/* envelope front */
.envelope-front{position:absolute;left:628px;top:63px;width:541px;height:362px}
.envelope-front .flap{position:absolute;left:0;top:0;width:541px;height:86px}
.envelope-front .body{position:absolute;left:0;top:85px;width:541px;height:277px;background:var(--paper);box-shadow:0 2px 8px rgba(0,0,0,.18)}
.envelope-front .brand{left:33px;top:24px}
.envelope-front .brand .wordmark{font-size:25px}
.envelope-front .brand .dot{width:24px;height:24px}
.envelope-front .brand .tagline{font-size:8px;margin-left:32px}
.envelope-front .sender-name{position:absolute;left:82px;top:73px;font-size:5px;font-weight:700;color:var(--ci-blue)}
.envelope-front .sender-address{position:absolute;left:80px;top:84px;display:flex;align-items:center;gap:4px;font-size:7px;color:#666}
.envelope-front .sender-address svg{width:8px;height:8px;fill:var(--ci-blue)}
.address-window{position:absolute;left:33px;top:155px;width:217px;height:87px;border:1px solid #c9c9c9;border-radius:12px;box-shadow:inset 0 2px 6px rgba(0,0,0,.15)}
.address-window p{position:absolute;left:42px;top:20px;font-size:7.3px;line-height:11.5px;color:#555}
.envelope-front .bands{left:0;right:0;top:257px}
.envelope-front .bands .rule.short{flex:0 0 44px}
.envelope-front .bands .url{font-size:12.5px}
.envelope-front .bands .url svg{width:12px;height:12px}

/* envelope back */
.envelope-back{position:absolute;left:631px;top:449px;width:543px;height:278px;background:var(--ci-blue);box-shadow:0 2px 8px rgba(0,0,0,.22)}
.envelope-back svg.fold{position:absolute;left:0;top:0;width:543px;height:100px}
.flap-mark{position:absolute;left:0;right:0;text-align:center;font-family:"Questrial",sans-serif;color:var(--ci-grey);letter-spacing:2px}
</style>
</head>
<body>
<div class="canvas">

  <!-- Letterhead -->
  <section class="letterhead" aria-label="Briefpapier">
    <div class="top-band"></div>

    <div class="brand">
      <div class="wordmark"><span class="dot"></span>Veltrano®</div>
      <div class="tagline">The Harbor Weavers</div>
    </div>

    <div class="sender">
      <div class="company">Veltrano GmbH</div>
      <div>Kornweg 9b</div>
      <div>D-85001 Auenried</div>
    </div>

    <ul class="contact-list">
      <li>+49 (0)8100-55 10 200
        <svg viewBox="0 0 10 10"><path d="M2 0.5 L3.6 2.8 L2.6 3.8 Q3.8 6.2 6.2 7.4 L7.2 6.4 L9.5 8 L8.2 9.5 Q1 8 0.5 1.8 Z"/></svg></li>
      <li>+49 (0)8100-55 10 281
        <svg viewBox="0 0 10 10"><rect x="2" y="0.5" width="6" height="3"/><rect x="0.5" y="4" width="9" height="4.5" rx="1"/></svg></li>
      <li>+49 (0)170-00 12 34 56
        <svg viewBox="0 0 10 10"><rect x="3" y="0.5" width="4" height="9" rx="1"/></svg></li>
      <li>Holger.Brink@veltrano-example.com
        <svg viewBox="0 0 10 10"><path d="M0.5 3 L5 0.5 L9.5 3 V9.5 H0.5 Z"/><path d="M1 3.5 L5 6 L9 3.5" fill="none" stroke="#fff" stroke-width=".8"/></svg></li>
    </ul>

    <div class="window-marks"><span class="tl"></span><span class="tr"></span><span class="bl"></span><span class="br"></span></div>
    <p class="window-address">Marlene Vossberg<br>Am Lindenhang 17<br>53111 Talheim<br>SCHWEIZ</p>

    <p class="return-line">Veltrano GmbH · Kornweg 9b · 85001 Auenried</p>

    <p class="recipient">Finanzamt Musterfeld<br>z.Hd. Herrn …<br>85300 Musterfeld</p>

    <p class="subject">Steuerliche Erfassung für Veltrano GmbH</p>
    <p class="body-text" style="top:324px">Sehr geehrter Herr …</p>
    <p class="body-text" style="top:351px">Mit freundlichen Grüßen</p>
    <p class="body-text" style="top:407px">Holger Brink</p>

    <span class="fold-mark" style="top:263px"></span>
    <span class="fold-mark" style="top:513px"></span>

    <div class="footer-brand"><span class="dot"></span>Veltrano GmbH</div>
    <div class="footer-col bank">Bankverbindung:<br>Hansabank AG Lindau<br>IBAN: DE00 1234 5678 0000 1111 22<br>BIC: HSBA DE 1L</div>
    <span class="footer-divider" style="left:306px"></span>
    <div class="footer-col tax">Steuernummer:<br>100/0000/0000<br>USt.- ID: DE 000000000</div>
    <span class="footer-divider" style="left:414px"></span>
    <div class="footer-col branch">Filiale:<br>Brunnenstraße 4<br>45000 Wellstadt</div>

    <div class="bands">
      <span class="rule short"></span>
      <span class="url"><svg viewBox="0 0 12 12"><circle cx="6" cy="6" r="5"/><path d="M1 6H11M6 1V11M6 1C3 4 3 8 6 11M6 1C9 4 9 8 6 11"/></svg>www.veltrano-example.com</span>
      <span class="rule"></span>
    </div>
  </section>

  <!-- Envelope front -->
  <section class="envelope-front" aria-label="Kuvert Vorderseite">
    <svg class="flap" viewBox="0 0 541 86" aria-hidden="true">
      <path d="M0 86 L30 8 Q33 0 42 0 H499 Q508 0 511 8 L541 86 Z" fill="var(--ci-blue)"/>
      <text x="270" y="50" text-anchor="middle" font-family="Questrial, sans-serif" font-size="14" letter-spacing="2" fill="var(--ci-grey)">Veltrano</text>
    </svg>
    <div class="body">
      <div class="brand">
        <div class="wordmark"><span class="dot"></span>Veltrano®</div>
        <div class="tagline">The Harbor Weavers</div>
      </div>
      <p class="sender-name">Veltrano GmbH</p>
      <p class="sender-address"><svg viewBox="0 0 10 10"><path d="M5 0.5 L9.5 5 H8 V9.5 H6 V6.5 H4 V9.5 H2 V5 H0.5 Z"/></svg>Kornweg 9b&nbsp;&nbsp;D-85001 Auenried</p>
      <div class="address-window"><p>Marlene Vossberg<br>Am Lindenhang 17<br>53111 Talheim<br>SCHWEIZ</p></div>
      <div class="bands">
        <span class="rule"></span>
        <span class="url"><svg viewBox="0 0 12 12"><circle cx="6" cy="6" r="5"/><path d="M1 6H11M6 1V11M6 1C3 4 3 8 6 11M6 1C9 4 9 8 6 11"/></svg>www.veltrano-example.com</span>
        <span class="rule short"></span>
      </div>
    </div>
  </section>

  <!-- Envelope back -->
  <section class="envelope-back" aria-label="Kuvert Rückseite">
    <svg class="fold" viewBox="0 0 543 100" aria-hidden="true">
      <path d="M0 2 L30 80 Q34 87 44 87 H499 Q509 87 513 80 L543 2" fill="none" stroke="#0a2236" stroke-width="2"/>
    </svg>
    <p class="flap-mark" style="top:38px;font-size:16px">Veltrano</p>
  </section>

</div>
</body>
</html>
```